Business Card design for sports marketing creative agency

We need a business card designed for a sports marketing agency.
Side 1: Vosk | 720
Gold Vosk 720 brand
Division of Vosk | a creative agency that focuses on athletes
Modern look
Info on Card:
vosk720.com
@vosk_720
Peter R. Lund
Director of Client Services
M: 555.287.4193
E. peter@vosk720.com
Side 2:
Red Vosk | a creative agency brand
Marketing Creative Agency
Modern look
Info on card:
Vosk | a creative agency (red logo)
voskstudio.com
@voskstudio
Target Market(s)
Pro athletes
Industry/Entity Type
Marketing
Look and feel
Each slider illustrates characteristics of the customer's brand and the style your logo design should communicate.

```html
<!DOCTYPE html>
<html lang="en">
<head>
<meta charset="utf-8">
<title>Vosk | 720 — Business Card</title>
<link rel="stylesheet" href="https://fonts.googleapis.com/css2?family=Open+Sans:wght@300;400;600;700&display=swap">
<style>
  :root {
    --bg: #c9c9c9;
    --card: #0b0b0b;
    --red: #d3121c;
    --red-dark: #7a0a10;
    --gold: #c9a23f;
    --white: #ffffff;
  }
  * { margin: 0; padding: 0; box-sizing: border-box; }
  html, body { width: 1200px; height: 894px; overflow: hidden; }
  body {
    background: var(--bg);
    font-family: "Open Sans", sans-serif;
    position: relative;
  }
  .card {
    position: absolute;
    left: 290px;
    width: 620px;
    height: 354px;
    background: var(--card);
    overflow: hidden;
    box-shadow: 0 10px 24px rgba(0,0,0,.25);
  }
  .card--studio { top: 62px; }
  .card--athlete { top: 478px; }
  .card__swoosh { position: absolute; inset: 0 0 auto 0; width: 620px; height: 80px; }

  .brand { position: absolute; display: flex; align-items: center; font-weight: 400; line-height: 1; }
  .brand__name { font-size: 44px; letter-spacing: 1px; }
  .brand__divider { width: 2px; height: 36px; margin: 0 12px; background: currentColor; }
  .brand__tagline { font-size: 24px; }
  .brand--red { color: var(--red); }
  .brand--gold { color: var(--gold); }

  .card--studio .brand { left: 170px; top: 104px; }
  .socials {
    position: absolute; left: 70px; right: 70px; top: 236px;
    display: flex; justify-content: space-between; list-style: none;
  }
  .socials__item { display: flex; align-items: center; gap: 10px; color: var(--white); font-size: 14px; }
  .socials__mark { width: 18px; height: 18px; background: var(--red); }
  .edge-tab { position: absolute; width: 22px; height: 38px; background: linear-gradient(var(--red), var(--red-dark)); }
  .card--studio .edge-tab { right: 0; top: 262px; }

  .card--athlete .brand { left: 150px; top: 70px; }
  .card--athlete .edge-tab { left: 0; top: 140px; width: 36px; height: 46px; }
  .person { position: absolute; left: 56px; top: 146px; }
  .person__name { color: var(--white); font-weight: 700; font-size: 26px; letter-spacing: .5px; line-height: 1.1; }
  .person__title { margin-top: 2px; color: var(--red); font-size: 11px; letter-spacing: 4px; text-transform: uppercase; }

  .contact {
    position: absolute; left: 360px; top: 220px; list-style: none;
    color: var(--white); font-weight: 600; font-size: 13px; line-height: 1.3;
  }
  .contact__item { display: flex; align-items: flex-start; gap: 12px; margin-bottom: 6px; }
  .contact__icon { width: 16px; height: 16px; flex: none; margin-top: 1px; fill: var(--red); }
</style>
</head>
<body>

<section class="card card--studio" aria-label="Vosk studio side">
  <svg class="card__swoosh" viewBox="0 0 620 80" aria-hidden="true">
    <defs>
      <linearGradient id="swoosh-studio" x1="0" x2="1">
        <stop offset="0" stop-color="#7a0a10"/><stop offset=".5" stop-color="#d3121c"/><stop offset="1" stop-color="#8a0c12"/>
      </linearGradient>
    </defs>
    <path d="M0 0 L0 40 C180 22 420 10 620 16 L620 0 Z" fill="url(#swoosh-studio)"/>
    <path d="M0 0 L0 32 C180 14 420 2 620 8 L620 0 Z" fill="#0b0b0b"/>
  </svg>
  <div class="brand brand--red">
    <span class="brand__name">Vosk</span>
    <span class="brand__divider"></span>
    <span class="brand__tagline">a creative agency</span>
  </div>
  <ul class="socials">
    <li class="socials__item"><span class="socials__mark"></span>voskstudio.com</li>
    <li class="socials__item"><span class="socials__mark"></span>@voskstudio</li>
    <li class="socials__item"><span class="socials__mark"></span>@vosk_720</li>
  </ul>
  <div class="edge-tab"></div>
</section>

<section class="card card--athlete" aria-label="Vosk 720 side">
  <svg class="card__swoosh" viewBox="0 0 620 80" aria-hidden="true">
    <defs>
      <linearGradient id="swoosh-athlete" x1="0" x2="1">
        <stop offset="0" stop-color="#d3121c"/><stop offset=".6" stop-color="#a80e16"/><stop offset="1" stop-color="#5a070b"/>
      </linearGradient>
    </defs>
    <path d="M0 0 L0 22 C200 30 420 48 620 70 L620 0 Z" fill="url(#swoosh-athlete)"/>
    <path d="M0 0 L0 14 C200 22 420 40 620 62 L620 0 Z" fill="#0b0b0b"/>
  </svg>
  <div class="brand brand--gold">
    <span class="brand__name">Vosk</span>
    <span class="brand__divider"></span>
    <span class="brand__name">720</span>
  </div>
  <div class="edge-tab"></div>
  <div class="person">
    <p class="person__name">PETER R. LUND</p>
    <p class="person__title">Director of Client Services</p>
  </div>
  <ul class="contact">
    <li class="contact__item">
      <svg class="contact__icon" viewBox="0 0 16 16" aria-hidden="true"><path d="M8 1 L15 8 H13 V15 H9.5 V10.5 H6.5 V15 H3 V8 H1 Z"/></svg>
      <span>214 9th floor, Harbor<br>Plaza Road</span>
    </li>
    <li class="contact__item">
      <svg class="contact__icon" viewBox="0 0 16 16" aria-hidden="true"><circle cx="8" cy="8" r="6.5" fill="none" stroke="#d3121c" stroke-width="1.4"/><path d="M1.5 8 H14.5 M8 1.5 V14.5" stroke="#d3121c" stroke-width="1.2"/><ellipse cx="8" cy="8" rx="3" ry="6.5" fill="none" stroke="#d3121c" stroke-width="1.2"/></svg>
      <span>vosk720.com</span>
    </li>
    <li class="contact__item">
      <svg class="contact__icon" viewBox="0 0 16 16" aria-hidden="true"><path d="M1 3 H15 V13 H1 Z"/><path d="M1 3 L8 9 L15 3" fill="none" stroke="#0b0b0b" stroke-width="1.2"/></svg>
      <span>E. peter@vosk720.com</span>
    </li>
    <li class="contact__item">
      <svg class="contact__icon" viewBox="0 0 16 16" aria-hidden="true"><path d="M4 1 L6.5 4.5 L5 6.5 C6 8.5 7.5 10 9.5 11 L11.5 9.5 L15 12 L13 15 C7 14.5 1.5 9 1 3 Z"/></svg>
      <span>M: 555.287.4193</span>
    </li>
  </ul>
</section>

</body>
</html>
```